Luxury tennis village/academy - Webdesign

We want to develop a cutting edge website for a luxury tennis academy. Academy is based in Russia and includes all the necessary amenities for comfortable stay: apartments, spa, tennis courts, training facilities, etc.
We would like to see a clean, simple and modern design (with implementation of all the current trends in web design, although our project has to be distinct and unique).
Color scheme: we would like to see colors present in our logos and all the current associated with tennis. We are open to your ideas and creativity on this front.
The final design should communicate simplicity, be user friendly and convey premium feel.
We woud like to see unique ideas in the design, unconventional techniques, etc.
We don't want standard template design!
Updates
We want to mention that this Tennis Academy has a light focus on nature, as the new material we have uploaded illustrates.
Additional comment to everyone!
We couldn't upload this file to the system: it is too big.
Thank you everyone for your submissions!
Industry/Entity Type
Training
Requirements
Must have
- We would like to see the designs for the following pages:
Home Page:
- Slideshow
- Short description and all the standard stuff
About Us:
- Description with some images
Services:
- Simple description of all of the provided services and possibility to book all of them on the website
! Important ! Develop small system for booking of the days of stay and registration for the courses
Booking and registration !
News:
- Creative layout to display recent news of the academy
Coaches:
- Image and short description of our staff.
Club / Gallery:
- Images and descriptions of the amenities in the territory.
We want a unique display of images: not just lines and rows filled with images
- One idea: an interactive map that displays images and description on mouseover or click on the object on the map (but again, we are open to all your ideas)
Contacts:
- Contact form, contacts, etc.
Sport Store:
- Basic layout for the goods and services provided by the sports store located in the academy
Prices:
- Price lists and ranges with a button leading to registration and booking
For pages like About Us and Services, it would be enough to develop one unified layout for all of them.

```html
<!DOCTYPE html>
<html lang="en">
<head>
<meta charset="utf-8">
<title>Greenhill Tennis — Home</title>
<link rel="stylesheet" href="https://fonts.googleapis.com/css2?family=Roboto:ital,wght@0,300;0,400;0,500;1,300&display=swap">
<style>
:root{
  --green:#2a9a2f;
  --green-dark:#2f7d1f;
  --nav-text:#555a5e;
  --header-bg:rgba(246,249,252,.94);
  --footer-bg:#ececec;
  --tab-icon:#c4c4c4;
  --label:#6a6a6a;
  --white:#ffffff;
}
*{margin:0;padding:0;box-sizing:border-box}
html,body{width:1200px;height:757px;overflow:hidden}
body{position:relative;font-family:"Roboto",Arial,sans-serif;color:var(--nav-text);background:#9fc4de}
.backdrop{position:absolute;inset:0;
  background:
    linear-gradient(180deg,#a6cdea 0%,#c7dfe8 20%,#9ba5a4 34%,#6f7f6e 48%,#c6cfcf 58%,#55666a 72%,#7d8f95 86%,#4a5a5f 100%);}
.backdrop::after{content:"";position:absolute;inset:0;
  background:radial-gradient(ellipse at 12% 55%,rgba(220,230,230,.55),transparent 45%),
             radial-gradient(ellipse at 90% 45%,rgba(60,90,60,.45),transparent 40%);}
.site-header{position:absolute;left:0;top:0;width:1200px;height:55px;background:var(--header-bg)}
.brand{position:absolute;left:79px;top:13px;display:flex;align-items:center;gap:8px;
  font-size:27px;font-weight:500;color:var(--green-dark);letter-spacing:-.5px}
.brand-dot{width:22px;height:22px;border-radius:50%;background:#8cc63f}
.main-nav{position:absolute;right:78px;top:0;display:flex;height:55px}
.main-nav a{position:relative;display:block;padding:17px 11px 0;font-size:16px;color:var(--nav-text);text-decoration:none}
.main-nav a.active{color:var(--green)}
.main-nav a.active::after{content:"";position:absolute;left:0;right:0;bottom:0;height:2px;background:var(--green)}
.main-nav a.active::before{content:"";position:absolute;left:50%;bottom:2px;margin-left:-3px;border:3px solid transparent;border-bottom-color:var(--green)}
.tagline{position:absolute;left:0;width:1200px;top:111px;text-align:center;font-size:25px;font-weight:300;font-style:italic;color:var(--green-dark)}
.slide{position:absolute;left:191px;top:205px;width:818px;height:339px;border:1px solid rgba(255,255,255,.85);overflow:hidden}
.slide-photo{position:absolute;inset:0;
  background:linear-gradient(180deg,#7fb1de 0%,#c9dcea 25%,#d8d6c8 38%,#b7b3a3 50%,#a65a3c 58%,#b0664a 72%,#5d8f35 84%,#4b7d2c 100%)}
.slide-caption{position:absolute;left:0;bottom:0;width:610px;height:66px;background:rgba(90,120,80,.55);
  padding:15px 18px 0;font-size:14px;line-height:18px;color:var(--white);font-weight:400}
.arrow{position:absolute;top:353px;width:44px;height:44px;border-radius:50%;background:rgba(255,255,255,.35)}
.arrow svg{display:block}
.arrow-prev{left:17px}
.arrow-next{left:1138px;background:rgba(255,255,255,.3)}
.section-tabs{position:absolute;left:0;top:697px;width:1200px;height:60px;background:var(--footer-bg)}
.tab{position:absolute;top:-23px;width:120px;margin-left:-60px;text-align:center}
.tab-bump{width:72px;height:72px;border-radius:50%;background:var(--footer-bg);margin:0 auto;position:relative;top:-2px}
.tab-bump span{position:absolute;left:14px;top:14px;width:44px;height:44px;border-radius:50%;background:var(--tab-icon)}
.tab-bump svg{position:absolute;left:0;top:0}
.tab-label{position:absolute;top:58px;left:0;width:120px;font-size:14px;font-weight:300;color:var(--label)}
.tab.current .tab-label{color:var(--green)}
</style>
</head>
<body>
<div class="backdrop" role="img" aria-label="Blurred photo of a lake with trees and sky reflected in the water"></div>

<header class="site-header">
  <div class="brand"><span>Greenhill Tennis</span><span class="brand-dot"></span></div>
  <nav class="main-nav">
    <a class="active" href="#">Home</a>
    <a href="#">About</a>
    <a href="#">Services</a>
    <a href="#">Club</a>
    <a href="#">Gallery</a>
    <a href="#">Contact</a>
  </nav>
</header>

<h1 class="tagline">Lorem ipsum dolor sit amet, consectetur adipiscing elit.</h1>

<div class="slide">
  <div class="slide-photo" role="img" aria-label="Photo of clay tennis courts with a dome hall and club houses under a cloudy sky"></div>
  <p class="slide-caption">Integer lectus sapien, suscipit quis elementum convallis, gravida eleifend augue.<br>Aliquam eu quam nec mauris ultricies fringilla eget id nulla. Aliquam tempor molestie justo.</p>
</div>

<a class="arrow arrow-prev" href="#" aria-label="Previous slide"><svg width="44" height="44" viewBox="0 0 44 44"><path d="M25 14 L17 22 L25 30" fill="none" stroke="#fff" stroke-width="4" stroke-linecap="round" stroke-linejoin="round"/></svg></a>
<a class="arrow arrow-next" href="#" aria-label="Next slide"><svg width="44" height="44" viewBox="0 0 44 44"><path d="M19 14 L27 22 L19 30" fill="none" stroke="#fff" stroke-width="4" stroke-linecap="round" stroke-linejoin="round"/></svg></a>

<nav class="section-tabs">
  <div class="tab" style="left:114px">
    <div class="tab-bump"><span></span><svg width="72" height="72" viewBox="0 0 72 72"><path d="M27 33 L36 41 L45 33" fill="none" stroke="#fff" stroke-width="4" stroke-linecap="round" stroke-linejoin="round"/></svg></div>
    <div class="tab-label">Recent News</div>
  </div>
  <div class="tab current" style="left:600px">
    <div class="tab-bump"><span></span><svg width="72" height="72" viewBox="0 0 72 72"><path d="M27 33 L36 41 L45 33" fill="none" stroke="#fff" stroke-width="4" stroke-linecap="round" stroke-linejoin="round"/></svg></div>
    <div class="tab-label">Services</div>
  </div>
  <div class="tab" style="left:1089px">
    <div class="tab-bump"><span></span><svg width="72" height="72" viewBox="0 0 72 72"><path d="M27 33 L36 41 L45 33" fill="none" stroke="#fff" stroke-width="4" stroke-linecap="round" stroke-linejoin="round"/></svg></div>
    <div class="tab-label">Club / Gallery</div>
  </div>
</nav>
</body>
</html>
```